Halvorsen Spa

We are a large Miami Beach spa and salon. I am still building our website but you can use it as a resource to gain a better understanding of who we are ....www.spaquillowave.com.

We offer a comprehensive list of services in hair, nails, massage, skin care, tanning, spray tanning and waxing and we offer high quality products for skin care, tanning and hair. We are open 7 days.

We would like to see a clean and simple menu that looks a lot like the one from "The Spa at Brightmere." In particular, we have a copy of a menu from their West Hollywood, CA location that is just beautiful. In the uploaded content you will see a sampling of that menu. We would like to see greys, blacks, silvers, whites and warm colors like reds and oranges. We specifically attempt to remain gender neutral so that we don't attract only girls (with pink colors and flowers etc). The final design should convey a simple, clean, friendly environment and the final product should be sized such that it is 1.) portable and 2.) inexpensive to print. We will be running thousands of these at a time so cost of printing is a consideration.

The booklet consists of two parts: one part is the standard menu with descriptions of services and products and photos etc (think of this as the sales piece that convinces a potential customer to visit) and will be stapled together like you would expect a small menu to be and should resemble the Brightmere menu. The prices should not be included in this part of the booklet that will be printed and stapled. The other part is a single insert and is removable and replaceable. I want this removable insert placed in the last page of the book in a folder pocket or something else that you can think of so that when it's time to change prices here that I am not throwing away all of the booklets....I am only replacing the inserts at the end of the menu booklet. Please design this single page insert so that should a customer remove it from the booklet and keep it, that it stands alone with our name, logo, website and phone number. This page can and probably will have to be 2 sided.

At the back of the booklet, I also want the polices to be printed in one page (think fine print in any sort of business dealing.)

With regard to the look and feel slider of economical v upmarket...we definitely want to convey we deliver upmarket services at reasonable prices. Think, world class services and products at reasonable, everyday prices.

With regard to the uploaded files:
I uploaded both EPS and TIF formats. The colors in those files are not the palette we want at all. The colors we want use for the circular logo must match the standard colors as depicted in the uploaded file "Halvorsentanrooms"

Target Market(s)

The target market is the average 20-35 year old in Miami Beach that cares about their appearance. The range of clientele is quite diverse.

Industry/Entity Type

Environment

Requirements
Must have
• It must have elegant and simple photographs that relate to the services being offered. We are selling a service set and an environment...so this menu should be reflect that goal. The logo should be repeated often throughout the book but in subtle ways.

Stock photos are fine as long as they don't seem obviously stock.

Should not have
• Nothing buddha like. Nothing themed. It should be all inclusive and not seek to identify with any particular group or gender.

Nothing that fits the stereotype of "Miami Beach." We want to represent ourselves in the same category as the best spas in the world because we moving everything we do in that direction. Think class!

```html
<!DOCTYPE html>
<html lang="en">
<head>
<meta charset="utf-8">
<title>Halvorsen Spa — Tanning Price Insert</title>
<link rel="stylesheet" href="https://fonts.googleapis.com/css2?family=Source+Sans+3:wght@300;400;600&display=swap">
<style>
  :root {
    --canvas: #ffffff;
    --photo-dark: #2a1f1d;
    --photo-warm: #6b3a2c;
    --photo-glow: #a9e4ea;
    --panel-top: #8c3020;
    --panel-mid: #9e3022;
    --panel-bottom: #c4222e;
    --frame: rgba(255, 255, 255, 0.55);
    --band: rgba(235, 235, 235, 0.62);
    --title-grey: #7b7b7b;
    --intro-ink: #2b2b2b;
    --menu-ink: #ffffff;
    --brand-ink: #eadcb6;
  }

  * { box-sizing: border-box; margin: 0; padding: 0; }

  html, body {
    width: 1200px;
    height: 600px;
    overflow: hidden;
    background: var(--canvas);
  }

  .spread {
    position: relative;
    width: 1200px;
    height: 600px;
    overflow: hidden;
    font-family: "Source Sans 3", "Myriad Pro", sans-serif;
    color: var(--menu-ink);
  }

  .spread__art {
    position: absolute;
    inset: 0;
    width: 1200px;
    height: 600px;
  }

  /* Left page title band */
  .feature-title {
    position: absolute;
    left: 48px;
    top: 462px;
    font-weight: 300;
    font-size: 42px;
    letter-spacing: 9px;
    color: var(--title-grey);
    line-height: 1;
  }

  .feature-intro {
    position: absolute;
    left: 313px;
    top: 466px;
    width: 266px;
    font-size: 8.3px;
    line-height: 10px;
    letter-spacing: 0.9px;
    color: var(--intro-ink);
  }

  /* Right page menu */
  .menu {
    position: absolute;
    left: 705px;
    top: 0;
    width: 440px;
    height: 600px;
    font-size: 10.2px;
    line-height: 12.5px;
  }

  .menu__abs { position: absolute; white-space: nowrap; }

  .menu__head {
    position: absolute;
    font-size: 11.8px;
    letter-spacing: 0.1px;
    white-space: nowrap;
  }

  .menu__body {
    position: absolute;
    left: 0;
    width: 432px;
  }

  .rate-table {
    position: absolute;
    border-collapse: collapse;
  }

  .rate-table td {
    padding: 0;
    height: 12.5px;
    white-space: nowrap;
    vertical-align: top;
  }

  .rate-table .qty { text-align: right; padding-right: 4px; }

  .brand {
    position: absolute;
    left: 1040px;
    top: 520px;
    width: 114px;
    display: flex;
    flex-direction: column;
    align-items: center;
    gap: 8px;
  }

  .brand__mark {
    width: 34px;
    height: 34px;
    border: 1.5px solid var(--brand-ink);
    border-radius: 50%;
  }

  .brand__name {
    font-size: 15px;
    font-weight: 400;
    letter-spacing: 1.5px;
    color: var(--brand-ink);
    white-space: nowrap;
  }
</style>
</head>
<body>
<main class="spread">
  <svg class="spread__art" viewBox="0 0 1200 600" aria-hidden="false">
    <defs>
      <linearGradient id="photoTone" x1="0" y1="0" x2="1" y2="1">
        <stop offset="0" stop-color="var(--photo-warm)"/>
        <stop offset="0.45" stop-color="#3e2c2a"/>
        <stop offset="1" stop-color="var(--photo-dark)"/>
      </linearGradient>
      <radialGradient id="photoGlow" cx="0.78" cy="0.45" r="0.45">
        <stop offset="0" stop-color="var(--photo-glow)" stop-opacity="0.55"/>
        <stop offset="1" stop-color="var(--photo-glow)" stop-opacity="0"/>
      </radialGradient>
      <linearGradient id="panelTone" x1="0" y1="0" x2="1" y2="1">
        <stop offset="0" stop-color="var(--panel-top)"/>
        <stop offset="0.55" stop-color="var(--panel-mid)"/>
        <stop offset="1" stop-color="var(--panel-bottom)"/>
      </linearGradient>
    </defs>

    <g role="img" aria-label="Photo: a glowing stand-up tanning bed in a dim room with paper screen walls and a potted bamboo plant">
      <rect class="photo" x="0" y="0" width="700" height="600" fill="url(#photoTone)"/>
      <rect class="photo-glow" x="0" y="0" width="700" height="600" fill="url(#photoGlow)"/>
    </g>

    <rect class="title-band" x="0" y="432" width="700" height="106" fill="var(--band)"/>

    <path class="price-panel" d="M665 0 H1200 V600 H556 Q665 560 665 417 Z" fill="url(#panelTone)"/>

    <rect class="trim-frame" x="19" y="18" width="1162" height="565" fill="none" stroke="var(--frame)" stroke-width="1.5"/>
  </svg>

  <h1 class="feature-title">TANNING</h1>
  <p class="feature-intro">Tina, conves conduct ta Simis sus, portis, eo esilicie mei potidees? Arbessules curnihil hacchil lesigiti clum et vit; nicaella ponloctur. Imo in tam poste, quam iam re confit. Ego publicesse te mac tenihil</p>

  <section class="menu">
    <h2 class="menu__head" style="left:0; top:63px;">TANNING</h2>
    <span class="menu__head" style="left:299px; top:63px;">Residents</span>
    <span class="menu__head" style="left:375px; top:63px;">Hotel Guests</span>

    <h3 class="menu__head" style="left:0; top:87px;">UV TANNING</h3>
    <p class="menu__body" style="top:101px;">Why sign up for unlimited tanning at The Halvorsen Spa? Here are a few reasons so many choose to tan with us.&nbsp; No hidden fees ever.&nbsp; No per-use fees.&nbsp; No eye protection surcharges.&nbsp; The tan tax is included.&nbsp; No contracts.&nbsp; No recurring billing.&nbsp; No membership cancellation policy.&nbsp; Newest beds on Miami Beach. Capped membership.&nbsp; It’s tanning made simple.</p>

    <h3 class="menu__head" style="left:0; top:162px;">UNLIMITED UV MEMBERSHIPS</h3>
    <p class="menu__body" style="top:177px;">You pick the membership. You pick the term. You pay in full. You tan. It’s that simple.</p>

    <span class="menu__abs" style="left:0; top:202px;">Silver Unlimited</span>
    <table class="rate-table" style="left:108px; top:202px;">
      <tr><td class="qty" style="width:18px">1</td><td style="width:44px">week</td><td>$19</td></tr>
      <tr><td class="qty">1</td><td>month</td><td>$29</td></tr>
      <tr><td class="qty">3</td><td>months</td><td>$79</td></tr>
      <tr><td class="qty">6</td><td>months</td><td>$139</td></tr>
      <tr><td class="qty">12</td><td>months</td><td>$249</td></tr>
    </table>

    <span class="menu__abs" style="left:224px; top:202px;">Gold Unlimited</span>
    <table class="rate-table" style="left:290px; top:202px;">
      <tr><td class="qty" style="width:18px">1</td><td style="width:44px">week</td><td>$29</td></tr>
      <tr><td class="qty">1</td><td>month</td><td>$39</td></tr>
      <tr><td class="qty">3</td><td>months</td><td>$99</td></tr>
      <tr><td class="qty">6</td><td>months</td><td>$189</td></tr>
      <tr><td class="qty">12</td><td>months</td><td>$349</td></tr>
    </table>

    <h3 class="menu__head" style="left:0; top:288px;">UV SERIES</h3>
    <p class="menu__body" style="top:302px; width:440px;">If you travel often or tan only every now and then, Prepaid Series cards may be the perfect fit for you. They can always be used and they never expire. Prepaid Series cards come in $49 and $99 denominations and significantly reduce your per-session price.</p>

    <span class="menu__abs" style="left:0; top:352px;">Prepaid $49 Series</span>
    <span class="menu__abs" style="left:83px; top:352px;">(22% savings)</span>
    <span class="menu__abs" style="left:149px; top:352px;">Each Silver Session $7 &amp; Each Gold Session $11</span>
    <span class="menu__abs" style="left:0; top:364px;">Prepaid $49 Series</span>
    <span class="menu__abs" style="left:83px; top:364px;">(44% savings)</span>
    <span class="menu__abs" style="left:149px; top:364px;">Each Silver Session $5 &amp; Each Gold Session $8</span>

    <h3 class="menu__head" style="left:0; top:401px;">UV SESSIONS</h3>
    <span class="menu__abs" style="left:0; top:416px;">Single Silver Sessions</span>
    <span class="menu__abs" style="left:133px; top:416px;">$9</span>
    <span class="menu__abs" style="left:149px; top:416px;">Single Gold Sessions</span>
    <span class="menu__abs" style="left:298px; top:416px;">$14</span>
    <span class="menu__abs" style="left:0; top:428px;">3 Silver Sessions</span>
    <span class="menu__abs" style="left:133px; top:428px;">$</span>
    <span class="menu__abs" style="left:149px; top:428px;">3 Gold Sessions</span>
    <span class="menu__abs" style="left:298px; top:428px;">$</span>
  </section>

  <div class="brand">
    <span class="brand__mark"></span>
    <span class="brand__name">HALVORSEN SPA</span>
  </div>
</main>
</body>
</html>
```